Restyle corporate identity (+ logo) for a road construction company

We need a new logo and stationary design for our company VELMOR path. VELMOR path® increases the road base strength, while reducing major costs and time of road construction. Attached some examples of the current design.

Our wishes for the new logo:
- Business look
- Style sheet
- Modern

More information: www.velmorpath-example.com
Updates

Target Market(s)

Government

Industry/Entity Type

Construction

Requirements
Must have
• Logo (with road sign) + text

```html
<!DOCTYPE html>
<html lang="en">
<head>
<meta charset="utf-8">
<title>VELMOR path — Stationery</title>
<link rel="stylesheet" href="https://fonts.googleapis.com/css2?family=Open+Sans:wght@400;600;700&display=swap">
<style>
:root{
  --bg:#dcdcdc;
  --paper:#ffffff;
  --paper-soft:#f3f3f3;
  --green:#9ac33c;
  --green-faint:#e6f0d4;
  --grey-dark:#76777a;
  --grey-light:#b1b2b4;
  --ink:#6d6e71;
}
*{box-sizing:border-box;margin:0;padding:0}
html,body{width:1200px;height:1048px;overflow:hidden}
body{background:radial-gradient(circle at 40% 45%,#f2f2f2 0%,var(--bg) 75%);font-family:"Open Sans",sans-serif;color:var(--ink);position:relative}
.sheet{position:absolute;background:var(--paper);box-shadow:0 6px 18px rgba(0,0,0,.18);overflow:hidden}
.brand{display:flex;align-items:center;gap:8px;font-weight:700;color:var(--ink);white-space:nowrap;letter-spacing:.5px}
.brand-square{background:var(--green);flex:none}
.bands{position:absolute;left:0;right:0;bottom:0;display:flex}
.bands span:nth-child(1){background:var(--green)}
.bands span:nth-child(2){background:var(--grey-dark)}
.bands span:nth-child(3){background:var(--grey-light);flex:1}
.faint-square{position:absolute;background:var(--green-faint);opacity:.8}
.contact{font-size:9px;line-height:1.45;font-weight:600}
.contact .label{color:var(--green);display:inline-block;width:40px}

/* letterhead */
.letterhead{left:50px;top:40px;width:440px;height:622px}
.letterhead .brand{position:absolute;left:36px;top:40px;font-size:24px}
.letterhead .brand-square{width:14px;height:14px}
.letterhead .rule{position:absolute;left:36px;top:80px;width:110px;height:1px;background:var(--grey-dark)}
.letterhead .contact{position:absolute;right:30px;top:130px;padding-left:12px;border-left:1px solid var(--grey-light)}
.letterhead .faint-square{left:250px;top:330px;width:130px;height:130px}
.letterhead .bands{height:22px}
.letterhead .bands span:nth-child(1){width:45%}
.letterhead .bands span:nth-child(2){width:27%}

/* business cards */
.card{top:40px;width:290px;height:166px}
.card-front{left:540px}
.card-back{left:860px}
.card .faint-square{left:14px;top:0;width:62px;height:50px}
.card .brand{position:absolute;font-size:17px}
.card .brand-square{width:10px;height:10px}
.card-front .brand{left:92px;top:56px}
.card-front .rule{position:absolute;left:92px;top:84px;width:70px;height:1px;background:var(--grey-dark)}
.card-back .brand{left:112px;top:36px}
.card-back .rule{position:absolute;left:112px;top:62px;width:70px;height:1px;background:var(--grey-dark)}
.card .bands{height:22px}
.card .bands span:nth-child(1){width:34%}
.card .bands span:nth-child(2){width:46%}
.card-front .web{position:absolute;left:108px;bottom:5px;font-size:8px;color:#fff;display:flex;align-items:center;gap:4px}
.card-front .web i{width:6px;height:6px;background:var(--green);display:block}
.person{position:absolute;left:16px;top:88px;display:flex;gap:6px;align-items:flex-start}
.person svg{flex:none}
.person .name{font-size:9px;font-weight:700;letter-spacing:.5px}
.person .role{font-size:6px}
.card-back .divider{position:absolute;left:168px;top:84px;width:1px;height:40px;background:var(--grey-light)}
.card-back .lines{position:absolute;left:176px;top:84px;font-size:6.5px;line-height:1.6}
.card-back .lines li{list-style:none;display:flex;align-items:center;gap:4px}
.card-back .lines li b{width:5px;height:5px;background:var(--green);display:block}
.card-back .addr{position:absolute;left:100px;bottom:4px;font-size:6.5px;color:#fff;line-height:1.2;text-align:center}

/* envelope */
.envelope{left:540px;top:236px;width:610px;height:300px;background:var(--paper-soft)}
.envelope .topband{position:absolute;left:0;right:0;top:0;height:14px;background:var(--green)}
.envelope .brand{position:absolute;left:58px;top:46px;font-size:26px}
.envelope .brand-square{width:15px;height:15px}
.envelope .rule{position:absolute;left:58px;top:88px;width:120px;height:1px;background:var(--grey-dark)}
.envelope .contact{position:absolute;left:58px;top:136px;font-size:10px}
.envelope .faint-square{right:30px;top:150px;width:110px;height:110px}
.envelope .bands{height:22px}
.envelope .bands span:nth-child(1){width:40%}
.envelope .bands span:nth-child(2){width:28%}
.envelope .web{position:absolute;right:28px;bottom:30px;font-size:11px;font-weight:700}

/* master lockup */
.lockup{position:absolute;left:56px;top:820px}
.lockup .brand{font-size:68px;gap:18px}
.lockup .brand-square{width:40px;height:40px}
.lockup .rule{margin-top:12px;width:210px;height:2px;background:var(--grey-dark)}
</style>
</head>
<body>

<section class="sheet letterhead" aria-label="Letterhead">
  <div class="brand"><span class="brand-square"></span>VELMOR path</div>
  <div class="rule"></div>
  <div class="contact">
    Address Line 1, Address Line2,<br>Address Line 3<br>
    <span class="label">Tel. -</span>+123 456 780<br>
    <span class="label">Fax. -</span>+123 456 789<br>
    <span class="label">Email -</span>yourmail@example.com<br>
    <span class="label">WEB -</span>www.velmorpath-example.com
  </div>
  <div class="faint-square"></div>
  <div class="bands"><span></span><span></span><span></span></div>
</section>

<section class="sheet card card-front" aria-label="Business card front">
  <div class="faint-square"></div>
  <div class="brand"><span class="brand-square"></span>VELMOR path</div>
  <div class="rule"></div>
  <div class="bands"><span></span><span></span><span></span></div>
  <div class="web"><i></i>www.velmorpath-example.com</div>
</section>

<section class="sheet card card-back" aria-label="Business card back">
  <div class="faint-square"></div>
  <div class="brand"><span class="brand-square"></span>VELMOR path</div>
  <div class="rule"></div>
  <div class="person">
    <svg width="12" height="12" viewBox="0 0 12 12" aria-hidden="true"><rect width="12" height="12" rx="2" fill="#9ac33c"/><circle cx="6" cy="4.5" r="2" fill="#fff"/><path d="M2.5 10.5c0-2 1.6-3.3 3.5-3.3s3.5 1.3 3.5 3.3z" fill="#fff"/></svg>
    <div><div class="name">YOUR NAME</div><div class="role">Position</div></div>
  </div>
  <div class="divider"></div>
  <ul class="lines">
    <li><b></b>+123 456 780</li>
    <li><b></b>+123 456 789</li>
    <li><b></b>yourmail@example.com</li>
    <li><b></b>www.velmorpath-example.com</li>
  </ul>
  <div class="bands"><span></span><span></span><span></span></div>
  <div class="addr">Address Line 1, Address Line 2,<br>Address Line 3</div>
</section>

<section class="sheet envelope" aria-label="Envelope">
  <div class="topband"></div>
  <div class="brand"><span class="brand-square"></span>VELMOR path</div>
  <div class="rule"></div>
  <div class="contact">
    Address Line 1, Address Line2,<br>Address Line 3<br>
    <span class="label">Email -</span>yourmail@example.com<br>
    <span class="label">Tel. -</span>+123 456 780<br>
    <span class="label">Fax. -</span>+123 456 789
  </div>
  <div class="faint-square"></div>
  <div class="web">www.velmorpath-example.com</div>
  <div class="bands"><span></span><span></span><span></span></div>
</section>

<section class="lockup" aria-label="Logo lockup">
  <div class="brand"><span class="brand-square"></span>VELMOR path</div>
  <div class="rule"></div>
</section>

</body>
</html>
```